Insurance Law Website

**Please note do not sell insurance, we are a law firm which specialises in Insurance law.**

We are a legal insurance firm based in Australia consisting of 150+ legal professionals.

Our initial budget for this project is around: $500

We require a design to meet the specification below, however we do want designers to come up with an interpretation of something modern but still professional, we need it to stand out above all other legal websites!

1. Responsive design
2. It should be a minimalist design, the use of background imagery is fine but we are looking to de-clutter the home page in particular and have additional content accessible through menu links to other areas such as publications, news, announcements and expert/staff pages, careers etc.
3. Something that stands out from a typical legal website.
4. The homepage should cater for a video which will contain a 'who we are' message from the CEO/Firm.
5. Colours used light/medium blues (eg: #8aabff, #bdd7fc), white
6. We also require a static information box on the page with the heading "THREE STATES, ONE FOCUS" - see image attached for full text of the box.

Visitors to our website should be aware we are an Insurance law firm, this can be achieved by using insurance focused full background imagery (no natural disasters such as floods, earthquakes etc) such as insurance buildings (Harwick building - London), international landmarks etc

Some websites we like certain aspects of;

http://pellambraithwaite.com/ - top image boxes
http://www.vantel.com.au/ - similar however prefer to use a FULL background image, with one full width text box at the bottom, navigation menu at the top with logo

However please don't take these examples as a sign of what the site MUST look like, please use your imagination to interpret your own vision.

Reason: Extended due to feedback provided and waiting for resubmission of designs. It appears that some people may be misunderstanding the brief, please review the brief in full before submitting any designs and let us know if you have any questions.

Reason: Apologies to those who are waiting for a decision we are reviewing and discussiing all submitted designs internally and waiting for some additional amendments to come in. We have extended the project a final time whilst we carry out our reviews. Please continue to submit any modifications and thanks again for everyone's input thus far. D+T

We have 3 days left of this project please keep submitting your designs. This is a guaranteed project.

D+T

Target Market(s)

Lawyers looking for publications, information, contact details of our lawyers and careers/job searches.

Industry/Entity Type

Insurance

Font styles to use
Sans Serif

Requirements
Must have
• Top menu to include:

Home (small icon)
Who We Are (text)
Experts (text)
Expertise (text)
Media (text)
- News (text)
- Publications (text)
Community Footprint (text)
Careers (text)
Contact (text/icon)
Search (icon - will expand on click to search in field)

Footer to include:

Copyright (text)
Privacy Policy (text)
Cookie policy (text)
Sitemap (text)
Contact (text/icon)
Chainbook (icon)
Print (icon)
Email (icon)

Should not have
• Stereotypical imagery such as legal scales, money bags, natural disasters etc. We are a professional firm and require designs to suit.

```html
<!DOCTYPE html>
<html lang="en">
<head>
<meta charset="utf-8">
<title>Dalton Tremaine – Insurance Law</title>
<link rel="stylesheet" href="https://fonts.googleapis.com/css2?family=Cinzel:wght@400;500&family=Open+Sans:wght@400;600;700&display=swap">
<style>
  :root {
    --navy: #0b4a9c;
    --blue: #0d4fa0;
    --heading: #2e62a8;
    --body-text: #6d90c6;
    --footer-text: #7b9ccc;
    --footer-link: #0b3e86;
    --rule: #a9bfdc;
    --white: #ffffff;
    --sky-top: #7fb3ea;
    --sky-mid: #2f78c9;
    --glass: #0c3f86;
    --office-dark: #3a2418;
    --office-mid: #7a4d2c;
    --player: #1aa3dc;
    --player-dark: #0a3a5a;
  }
  * { box-sizing: border-box; margin: 0; padding: 0; }
  html, body { width: 1200px; height: 965px; overflow: hidden; background: var(--white); }
  body { position: relative; font-family: "Open Sans", sans-serif; }

  .brand {
    position: absolute; left: 500px; top: 18px; width: 210px;
    color: var(--blue); font-family: "Open Sans", sans-serif; font-weight: 400;
    font-size: 38px; line-height: 36px; text-align: center; letter-spacing: 0.5px;
  }

  .main-nav {
    position: absolute; left: 6px; top: 117px; width: 1194px; height: 43px;
    border-top: 1px solid var(--rule); border-bottom: 1px solid var(--rule);
    display: flex; align-items: center;
  }
  .nav-home {
    width: 65px; height: 43px; margin-top: -1px; background: var(--navy);
    display: flex; align-items: center; justify-content: center;
  }
  .nav-links {
    display: flex; justify-content: space-between; align-items: center;
    flex: 1; padding: 0 96px 0 11px; list-style: none;
  }
  .nav-links li {
    font-family: "Cinzel", serif; font-weight: 500; font-size: 16px; color: var(--blue);
    display: flex; align-items: center; gap: 6px; white-space: nowrap;
  }
  .nav-search { position: absolute; right: 14px; top: 11px; }

  .hero-photo {
    position: absolute; left: 9px; top: 176px; width: 764px; height: 318px;
    background: linear-gradient(160deg, var(--glass) 0%, var(--sky-mid) 35%, var(--sky-top) 55%, var(--sky-mid) 75%, var(--glass) 100%);
  }
  .ceo-video {
    position: absolute; left: 786px; top: 176px; width: 414px; height: 318px;
    background: linear-gradient(120deg, var(--office-dark), var(--office-mid) 55%, var(--office-dark));
  }
  .play-button { position: absolute; left: 177px; top: 89px; }
  .player-bar {
    position: absolute; left: 0; bottom: 0; width: 100%; height: 24px;
    background: var(--player); display: flex; align-items: center; padding: 0 6px; gap: 6px;
  }
  .player-track { flex: 1; height: 6px; background: #0a5e88; border-radius: 3px; }
  .player-time {
    background: var(--player-dark); color: var(--white); font-size: 10px; padding: 2px 8px; border-radius: 3px;
  }

  .focus-band {
    position: absolute; left: 7px; top: 501px; width: 1193px; height: 86px;
    background: var(--navy); color: var(--white); display: flex; align-items: center;
  }
  .focus-title {
    font-family: "Cinzel", serif; font-weight: 500; font-size: 41px;
    width: 585px; padding-left: 18px; white-space: nowrap;
  }
  .focus-text { font-size: 14.5px; line-height: 18px; width: 595px; }

  .section-title {
    font-family: "Cinzel", serif; font-weight: 400; font-size: 43px;
    color: var(--heading); line-height: 1;
  }
  .who-we-are { position: absolute; left: 21px; top: 654px; width: 700px; }
  .latest-news { position: absolute; left: 786px; top: 654px; width: 404px; }
  .section-body { color: var(--body-text); font-size: 14.4px; line-height: 18px; margin-top: 6px; }
  .news-headline { color: #5a84c0; font-size: 16.5px; font-weight: 700; margin-top: 6px; }
  .latest-news .section-body { margin-top: 0; font-size: 14px; }
  .more-link { color: var(--heading); font-size: 14px; font-weight: 700; margin-top: 14px; display: block; text-decoration: none; }

  .site-footer {
    position: absolute; left: 6px; top: 852px; width: 1194px; height: 113px;
    border-top: 1px solid var(--rule);
  }
  .footer-links { position: absolute; left: 7px; top: 18px; display: flex; gap: 16px; list-style: none; }
  .footer-links li, .footer-contact h3 { font-size: 14px; color: var(--footer-link); font-weight: 400; }
  .copyright { position: absolute; left: 7px; top: 42px; font-size: 13px; color: var(--footer-text); }
  .copyright strong { font-size: 14px; }
  .footer-contact { position: absolute; left: 463px; top: 18px; }
  .footer-contact p { font-size: 14px; color: var(--footer-text); line-height: 18px; margin-top: 6px; }
  .footer-icons { position: absolute; right: 10px; top: 21px; display: flex; gap: 12px; }
  .footer-icon {
    width: 52px; height: 52px; border-radius: 50%; background: var(--navy);
    display: flex; align-items: center; justify-content: center;
    color: var(--white); font-size: 9px; font-weight: 600;
  }
</style>
</head>
<body>

<div class="brand">dalton<br>tremaine</div>

<nav class="main-nav">
  <div class="nav-home">
    <svg width="28" height="24" viewBox="0 0 28 24" aria-label="Home">
      <path d="M2 12 L14 2 L26 12" fill="none" stroke="#fff" stroke-width="3"/>
      <rect x="6" y="11" width="16" height="11" fill="#fff"/>
      <rect x="12" y="15" width="4" height="7" fill="#0b4a9c"/>
    </svg>
  </div>
  <ul class="nav-links">
    <li>Who We Are</li>
    <li>Experts</li>
    <li>Expertise</li>
    <li>Media</li>
    <li>News</li>
    <li>Publications</li>
    <li>Community Footprint</li>
    <li>Careers</li>
    <li>
      <svg width="24" height="24" viewBox="0 0 24 24" aria-hidden="true">
        <circle cx="12" cy="12" r="10.5" fill="none" stroke="#0d4fa0" stroke-width="1.6"/>
        <path d="M8.5 6.5 l2 0 l1 3 l-1.5 1.2 q1 2.2 3 3.3 l1.3 -1.5 l3 1 l0 2 q-1 1.5 -3 1 q-5 -2 -6.5 -7 q-0.5 -2 0.7 -3z" fill="#0d4fa0"/>
      </svg>Contact
    </li>
  </ul>
  <svg class="nav-search" width="22" height="22" viewBox="0 0 22 22" aria-label="Search">
    <circle cx="9" cy="9" r="6.5" fill="none" stroke="#0d4fa0" stroke-width="2.4"/>
    <line x1="14" y1="14" x2="20" y2="20" stroke="#0d4fa0" stroke-width="2.8" stroke-linecap="round"/>
  </svg>
</nav>

<div class="hero-photo" role="img" aria-label="Photograph of glass office towers rising into a blue sky"></div>

<div class="ceo-video" role="img" aria-label="Video still of the firm's chief executive seated at a desk in a wood-panelled office">
  <svg class="play-button" width="94" height="94" viewBox="0 0 94 94" aria-label="Play video">
    <circle cx="47" cy="47" r="43" fill="rgba(255,255,255,0.35)" stroke="#fff" stroke-width="6"/>
    <path d="M36 26 L70 47 L36 68z" fill="#fff"/>
  </svg>
  <div class="player-bar">
    <svg width="56" height="14" viewBox="0 0 56 14" aria-hidden="true">
      <path d="M2 1 L12 7 L2 13z" fill="#0a3a5a"/>
      <path d="M30 1 L23 7 L30 13z M37 1 L30 7 L37 13z" fill="#0a3a5a"/>
      <path d="M42 1 L49 7 L42 13z M49 1 L56 7 L49 13z" fill="#0a3a5a"/>
    </svg>
    <div class="player-track"></div>
    <span class="player-time">00:00:00</span>
  </div>
</div>

<section class="focus-band">
  <h2 class="focus-title">THREE STATES,ONE FOCUS</h2>
  <p class="focus-text">Our sole focus is insurance law and we act for diverse range of risk carriers, underwriting agents, brokers and corporate insureds relevant to litigious and general advisory services.</p>
</section>

<section class="who-we-are">
  <h2 class="section-title">WHO WE ARE</h2>
  <p class="section-body">Lorem ipsum dolor sit amet, consectetur adipisicing elit, sed do eiusmod tempor incididunt ut labore et dolore magna aliqua. Ut enim ad minim veniam, quis nostrud exercitation ullamco laboris nisi ut aliquip ex ea commodo consequat. Duis aute irure dolor in reprehenderit in voluptate velit esse cillum dolore eu fugiat nulla pariatur. Excepteur sint occaecat cupidatat non proident, sunt in culpa qui officia deserunt mollit anim id est laborum.</p>
</section>

<section class="latest-news">
  <h2 class="section-title">NEWS</h2>
  <h3 class="news-headline">Sed ut perspiciatis unde omnis</h3>
  <p class="section-body">Iste natus error sit voluptatem accusantium doloremque laudantium, totam rem aperiam, eaque ipsa quae ab i...</p>
  <a class="more-link" href="#">+ more news</a>
</section>

<footer class="site-footer">
  <ul class="footer-links">
    <li>Privacy Policy</li>
    <li>Cookie policy</li>
    <li>Sitemap</li>
  </ul>
  <p class="copyright"><strong>Company Name</strong> © 2013. All Rights Reserved</p>
  <div class="footer-contact">
    <h3>Contact us</h3>
    <p>4120 Harbour Lane Glasgow, G12 7QX.<br>Phone: +1 555 014 2290</p>
  </div>
  <div class="footer-icons">
    <div class="footer-icon">Chainbook</div>
    <div class="footer-icon">
      <svg width="30" height="28" viewBox="0 0 30 28" aria-label="Print">
        <rect x="8" y="1" width="14" height="7" fill="#fff"/>
        <rect x="1" y="9" width="28" height="12" rx="2" fill="#fff"/>
        <rect x="7" y="15" width="16" height="12" fill="#fff" stroke="#0b4a9c" stroke-width="2"/>
        <line x1="10" y1="20" x2="20" y2="20" stroke="#0b4a9c" stroke-width="1.5"/>
        <line x1="10" y1="23" x2="20" y2="23" stroke="#0b4a9c" stroke-width="1.5"/>
      </svg>
    </div>
    <div class="footer-icon">
      <svg width="32" height="22" viewBox="0 0 32 22" aria-label="Email">
        <rect x="1" y="1" width="30" height="20" rx="2" fill="#fff"/>
        <path d="M2 2 L16 13 L30 2" fill="none" stroke="#0b4a9c" stroke-width="2"/>
        <path d="M2 20 L12 11 M30 20 L20 11" stroke="#0b4a9c" stroke-width="1.5"/>
      </svg>
    </div>
  </div>
</footer>

</body>
</html>
```